High quality childcare centre needs a roadside banner

We need a banner designed that advertises our achievement of being rated Exceeding National Quality Standard. Which is the highest rating you can be award as part of the assessment and rating process.

Attached pdf is purely an example although the text as it stands needs to be incorporated.

Please see below for the corporate colors:

Magenta
C-0 M-100 Y-33 K-10
bf00bf

Green
C-78 M-0 Y-100 K-0
00bf00

Target Market(s)

Parents of young children that need childcare

Industry/Entity Type

Childcare

Font styles to use
Sans Serif

Requirements
Must have
• As it is a roadside banner the text should be big, bold and easy to read therefore do not use serif fonts
• Please change found to find
• Logo - see attached
• Supplied wording - see attached
• The specs for the banner are 4m x 1.25m or 4000mm x 1250mm
• The files need to be in the following format:
• jpg, eps and ai.
• Bleeds if relevant
Nice to have
• Other marketing road signs incorporate the attached 'grobold' font
• We also have a motto - 'out of little things, big things grow'
Should not have
• Serif fonts

```html
<!DOCTYPE html>
<html lang="en">
<head>
<meta charset="utf-8">
<title>Small Sprouts – Exceeding National Quality Standard</title>
<link rel="stylesheet" href="https://fonts.googleapis.com/css2?family=Lato:wght@700;900&family=Lilita+One&display=swap">
<style>
  :root {
    --magenta: #d62b6b;
    --green: #34a84a;
    --green-dark: #1f7a30;
    --white: #ffffff;
    --edge-grey: #9a9a9a;
    --art-warm: #f0a65a;
    --art-cool: #c95b8f;
  }
  html, body {
    margin: 0;
    padding: 0;
    overflow: hidden;
    background: var(--white);
  }
  .banner {
    position: relative;
    width: 1200px;
    height: 500px;
    overflow: hidden;
    background: var(--magenta);
    font-family: "Lato", Arial, sans-serif;
  }
  .banner__curve {
    position: absolute;
    inset: 0;
    width: 1200px;
    height: 500px;
  }
  .banner__intro {
    position: absolute;
    left: 346px;
    top: 46px;
    margin: 0;
    color: var(--white);
    font-weight: 700;
    font-size: 39px;
    letter-spacing: 0.2px;
  }
  .rating {
    margin: 0;
    font-family: "Lilita One", "Arial Black", sans-serif;
    font-weight: 400;
    color: var(--white);
    text-shadow: 3px 4px 4px rgba(90, 0, 30, 0.35);
    line-height: 1;
  }
  .rating__line {
    position: absolute;
    display: block;
    font-size: 82px;
    white-space: nowrap;
  }
  .rating__line--one { left: 432px; top: 138px; }
  .rating__line--two { left: 502px; top: 222px; }
  .rating__line--three { left: 818px; top: 310px; }

  .reader-art {
    position: absolute;
    left: 920px;
    top: 6px;
    width: 250px;
    height: 214px;
    border-radius: 40% 40% 30% 30%;
    background: radial-gradient(circle at 50% 55%, var(--art-warm) 0%, var(--art-cool) 55%, rgba(214, 43, 107, 0) 75%);
  }

  .ribbon {
    position: absolute;
    left: 476px;
    top: 400px;
    width: 724px;
    height: 68px;
  }
  .ribbon__shape {
    position: absolute;
    left: 0;
    top: -10px;
    width: 724px;
    height: 78px;
  }
  .ribbon__text {
    position: absolute;
    right: 24px;
    top: 8px;
    margin: 0;
    color: var(--white);
    font-weight: 700;
    font-size: 37px;
    white-space: nowrap;
  }

  .brand {
    position: absolute;
    left: 44px;
    top: 340px;
    margin: 0;
    font-family: "Lilita One", "Arial Black", sans-serif;
    font-weight: 400;
    font-size: 62px;
    color: var(--green);
    white-space: nowrap;
  }
</style>
</head>
<body>
  <main class="banner">
    <svg class="banner__curve" viewBox="0 0 1200 500" aria-hidden="true">
      <path d="M0,0 L128,0 Q468,160 536,500 L0,500 Z" fill="var(--edge-grey)"/>
      <path d="M0,0 L116,0 Q452,166 516,500 L0,500 Z" fill="var(--white)"/>
    </svg>

    <p class="banner__intro">This service is rated</p>

    <h1 class="rating">
      <span class="rating__line rating__line--one">Exceeding</span>
      <span class="rating__line rating__line--two">National Quality</span>
      <span class="rating__line rating__line--three">Standard</span>
    </h1>

    <div class="reader-art" role="img" aria-label="Illustration of a child reading a book beside a stack of books, with colourful letters floating above"></div>

    <div class="ribbon">
      <svg class="ribbon__shape" viewBox="0 0 724 78" aria-hidden="true">
        <polygon points="0,0 14,10 14,20 0,20" fill="var(--green-dark)"/>
        <rect x="0" y="10" width="724" height="68" fill="var(--green)"/>
      </svg>
      <p class="ribbon__text">Come in and find out why.....</p>
    </div>

    <p class="brand">Small Sprouts</p>
  </main>
</body>
</html>
```